Modern Design for Eyecare business - Vision Center, Optometry, Eye Doctors, Health Care

Create a sleek, modern, sharp homepage design for a eyecare center in Oklahoma City, OK. The vision center provides eyecare health services along with prescription eyewear.

I have included the logo which should be the basis of the designs look and feel. No other imagery was given so feel free to include stock photos and illustrations that you believe give the design a fresh look.

Please do not include stock photos of people/humans

I have included a document that provides some verbiage for the design as well as the designs main navigation.

They have an existing website http://www.bluepineoptics.example/ but are not happy with it. The new design should be different than their existing design.

List of websites for inspiration:
http://www.harborfaith.example
https://www.meadowlenspartners.example
http://www.brightsmiledental.example/
https://www.keltro.example

Target Market(s)

all ages

industry: Health, Eyewear, Eyecare, Optometry

Industry/Entity Type

Health

Number of Pages Required

1 page

Requirements
Must have
• Light color scheme that matches logo colors.
• Sophisticated, sleek design that resembles the logo's style.
Nice to have
• Large, full width visual banner with a 'contact us, etc' call-to-action between header and homepage content
Should not have
• No stock images of people/humans.
• Other forms of stock photos/illustrations are fine.

```html
<!DOCTYPE html>
<html lang="en">
<head>
<meta charset="utf-8">
<title>Bluepine Optics – Vision Center, Oklahoma City</title>
<link rel="stylesheet" href="https://fonts.googleapis.com/css2?family=Open+Sans:wght@400;600&family=Roboto+Condensed:wght@400;700&family=Roboto:wght@400;500&display=swap">
<style>
:root{
  --navy:#2c3e55;
  --nav-blue:#6f93cf;
  --nav-active:#2f4a6a;
  --brand:#3f6aa8;
  --text:#333a44;
  --muted:#6b7380;
  --footer-bg:#f2f3f5;
  --footer-bar:#2b2d31;
  --badge:#dfe3ea;
  --white:#ffffff;
}
*{margin:0;padding:0;box-sizing:border-box}
html,body{width:1200px;height:2752px;overflow:hidden;background:var(--white)}
body{position:relative;font-family:"Open Sans",Arial,sans-serif;color:var(--text)}
.abs{position:absolute}
.cond{font-family:"Roboto Condensed","Arial Narrow",sans-serif}

/* header */
.site-header{left:0;top:0;width:1200px;height:130px}
.brand{left:97px;top:36px;display:flex;align-items:center;gap:12px}
.brand-dot{width:30px;height:30px;border-radius:50%;background:var(--brand)}
.brand-name{font-size:31px;color:var(--navy);font-weight:400}
.request{left:683px;top:32px;font-family:"Roboto",sans-serif;font-size:19px;color:var(--brand)}
.phone{left:680px;top:58px;font-family:"Roboto",sans-serif;font-size:27px;color:var(--navy);font-weight:500;letter-spacing:.5px}
.btn-schedule{left:891px;top:43px;width:210px;height:40px;background:linear-gradient(#3a4a60,#232f3f);color:#fff;font-family:"Roboto",sans-serif;font-size:13px;font-weight:500;display:flex;align-items:center;justify-content:center;border-radius:3px}

.main-nav{left:0;top:130px;width:1200px;height:52px;background:linear-gradient(#7b9dd6,#6289c8);display:flex;padding-left:99px}
.main-nav a{font-family:"Roboto",sans-serif;font-size:15px;color:#fff;text-decoration:none;height:52px;display:flex;align-items:center;padding:0 27px}
.main-nav a.active{background:var(--nav-active);padding:0 36px}

/* hero */
.hero{left:0;top:182px;width:1200px;height:493px;background:linear-gradient(100deg,#8ea7cf 0%,#7a93bd 40%,#55698f 75%,#3a3f55 100%)}
.hero-title{left:97px;top:305px;font-size:42px;line-height:48px;font-weight:700;color:#fff;letter-spacing:.5px}
.hero-text{left:99px;top:412px;width:350px;font-size:13px;line-height:20px;color:#eef3fb}
.btn-new{left:99px;top:493px;width:127px;height:39px;background:linear-gradient(#6e93d3,#4a72b6);color:#fff;font-family:"Roboto",sans-serif;font-size:14px;display:flex;align-items:center;justify-content:center;border-radius:3px}

/* feature cards */
.feature-panel{left:99px;top:635px;width:1002px;height:415px;background:#fff;border-top:3px solid var(--nav-blue);box-shadow:0 10px 18px rgba(0,0,0,.12)}
.feature{top:662px;width:308px}
.feature .photo{width:308px;height:181px;border:1px solid #ddd}
.feature h3{margin-top:28px;font-family:"Roboto",sans-serif;font-size:17px;font-weight:400;color:#222}
.feature p{margin-top:12px;font-size:11.5px;line-height:18px;color:var(--muted)}
.feature .more{margin-top:18px;font-family:"Roboto",sans-serif;font-size:11.5px;color:#444;display:flex;align-items:center;gap:8px}
.arrow-dot{width:11px;height:11px;border-radius:50%;background:#444;display:inline-flex;align-items:center;justify-content:center}

/* section headings */
.section-head{display:flex;align-items:center;justify-content:center;gap:14px;width:1200px;left:0}
.section-head .mark{width:30px;height:30px;border-radius:50%;background:var(--brand)}
.section-head h2{font-size:32px;font-weight:400;color:#1f2732}
.on-dark .mark{background:#fff}
.on-dark h2{color:#fff}

.welcome-text{left:200px;top:1136px;width:800px;text-align:center;font-size:11.5px;line-height:21px;color:var(--muted)}

/* services band */
.services{left:0;top:1243px;width:1200px;height:454px;background:linear-gradient(90deg,#6f90cd,#7396d2 50%,#6a8cc8)}
.service{top:1370px;width:240px;text-align:center}
.service .circle{width:118px;height:118px;margin:0 auto;border-radius:50%;background:#fff;border:4px solid #5a7bb6;display:flex;align-items:center;justify-content:center}
.service h3{margin-top:22px;font-family:"Roboto",sans-serif;font-size:17px;font-weight:400;color:#fff}
.service p{margin:14px auto 0;width:236px;font-size:11px;line-height:20px;color:#eef3fb;height:60px}
.service .read{display:inline-block;margin-top:14px;background:#fff;color:#3a4a60;font-family:"Roboto",sans-serif;font-size:11.5px;padding:7px 11px;border-radius:2px}

/* why us */
.why-photo{left:114px;top:1763px;width:408px;height:319px;background:linear-gradient(135deg,#f4f4f2,#d9dbd8 60%,#b9bcb8);border:1px solid #ccc}
.why-head{left:555px;top:1762px;display:flex;align-items:center;gap:12px}
.why-head .mark{width:28px;height:28px;border-radius:50%;background:var(--brand)}
.why-head h2{font-size:31px;font-weight:400;color:#1f2732}
.why-list{left:560px;top:1822px;width:540px;list-style:none}
.why-list li{display:flex;gap:12px;font-size:11.5px;line-height:17px;color:var(--text);margin-bottom:13px}
.why-list svg{flex:none;margin-top:3px}

/* experts band */
.experts{left:0;top:2150px;width:1200px;height:293px;background:linear-gradient(90deg,#3c5f8a,#46699a 50%,#3a5c86)}
.experts-text{left:140px;top:2273px;width:920px;text-align:center;font-size:12px;line-height:23px;color:#fff}

/* footer */
.footer{left:0;top:2443px;width:1200px;height:257px;background:var(--footer-bg)}
.partner-badge{left:100px;top:2527px;width:124px;height:96px;border-radius:50%;background:var(--badge)}
.footer-col h4{font-family:"Roboto",sans-serif;font-size:16px;font-weight:400;color:#222;letter-spacing:.4px}
.quick{left:325px;top:2478px}
.quick ul{list-style:none;margin-top:14px}
.quick li{font-size:12px;color:var(--muted);line-height:22px;display:flex;align-items:center;gap:9px}
.quick li::before{content:"";width:8px;height:8px;border-radius:50%;background:#5b7fbf}
.newsletter{left:534px;top:2478px;width:295px}
.newsletter p{margin-top:14px;font-size:11.5px;line-height:18px;color:var(--muted)}
.field{width:290px;height:39px;background:#fff;border:1px solid #e2e4e8;font-size:11.5px;color:#555;padding-left:14px;display:flex;align-items:center}
.subscribe{position:absolute;right:-1px;top:-1px;width:96px;height:41px;background:#5b80c4;color:#fff;font-size:12px;display:flex;align-items:center;justify-content:center}
.contact{left:881px;top:2478px;width:240px}
.contact .addr{margin-top:14px;font-size:12px;line-height:20px;color:var(--muted)}
.contact .row{display:flex;align-items:center;gap:12px;font-size:12px;color:var(--muted);margin-top:8px}
.socials{display:flex;gap:6px;margin-top:14px}
.socials span{width:22px;height:22px;border-radius:50%;border:1px solid #999}
.bottom-bar{left:0;top:2700px;width:1200px;height:52px;background:var(--footer-bar);color:#ddd;font-size:11.5px;display:flex;align-items:center;justify-content:center}
</style>
</head>
<body>

<header class="abs site-header">
  <div class="abs brand"><span class="brand-dot"></span><span class="brand-name">Bluepine Optics</span></div>
  <div class="abs request">Request appoitment</div>
  <div class="abs phone">405-555-0174</div>
  <div class="abs btn-schedule">SCHEDULE APPOINTMENT</div>
</header>

<nav class="abs main-nav">
  <a class="active">Home</a><a>Vision Services</a><a>Vision Health</a><a>Patient Info</a><a>Patient Reviews</a><a>Schedule Appointment</a><a>Contact Us</a>
</nav>

<section class="abs hero" role="img" aria-label="Close-up photograph of a blue eye in soft light"></section>
<h1 class="abs hero-title cond">BLUEPINE<br>OPTICS</h1>
<p class="abs hero-text">Caring eye exams and modern eyewear for every age, with friendly doctors right here in the heart of the city.</p>
<div class="abs btn-new">NEW PATIENTS</div>

<div class="abs feature-panel"></div>
<article class="abs feature" style="left:115px">
  <div class="photo" role="img" aria-label="Optometry exam equipment" style="background:linear-gradient(135deg,#eef0f2,#b6bcc4 55%,#5c6470)"></div>
  <h3>Opening Your Eyes To Clearer Vision</h3>
  <p>Thorough eye exams using modern tools so that small changes in your sight are found early and treated well.</p>
  <div class="more">CLICK HERE <span class="arrow-dot"><svg width="5" height="7" viewBox="0 0 5 7"><path d="M1 0.5 4 3.5 1 6.5" stroke="#fff" stroke-width="1.4" fill="none"/></svg></span></div>
</article>
<article class="abs feature" style="left:445px">
  <div class="photo" role="img" aria-label="Two contact lenses on a reflective surface" style="background:linear-gradient(135deg,#f5f6f8,#c9d6ec 45%,#8a7fc6 80%,#6b5fb0)"></div>
  <h3>A Personalized Approach To Vision</h3>
  <p>Every visit is shaped around your needs, from lens choices to comfort, style, budget and daily habits.</p>
  <div class="more">CLICK HERE <span class="arrow-dot"><svg width="5" height="7" viewBox="0 0 5 7"><path d="M1 0.5 4 3.5 1 6.5" stroke="#fff" stroke-width="1.4" fill="none"/></svg></span></div>
</article>
<article class="abs feature" style="left:775px">
  <div class="photo" role="img" aria-label="Contact lens being placed near an eye" style="background:linear-gradient(135deg,#d9a98e,#b98a72 50%,#7f6a63)"></div>
  <h3>Committed To Excellence In Vision Care</h3>
  <p>Skilled doctors and caring staff who hold every exam, fitting and follow up to a very high standard.</p>
  <div class="more">CLICK HERE <span class="arrow-dot"><svg width="5" height="7" viewBox="0 0 5 7"><path d="M1 0.5 4 3.5 1 6.5" stroke="#fff" stroke-width="1.4" fill="none"/></svg></span></div>
</article>

<div class="abs section-head" style="top:1086px"><span class="mark"></span><h2 class="cond">WELCOME TO BLUEPINE OPTICS</h2></div>
<p class="abs welcome-text">Our welcoming staff has one common goal – providing you with the best vision care possible and assisting you in finding you the finest eyewear that suits your lifestyle. While many big chain stores employ sales consultants to sell you glasses or contacts, our practice is comprised of knowledgeable individuals whose primary goal is to provide you with a high level of customer service all while ensuring you get the eye care you need and deserve.</p>

<section class="abs services" role="img" aria-label="Faint close-up of an eye behind blue tint"></section>
<div class="abs section-head on-dark" style="top:1285px"><span class="mark"></span><h2 class="cond">VISION SERVICES</h2></div>

<div class="abs service" style="left:93px">
  <div class="circle"><svg width="46" height="40" viewBox="0 0 46 40"><rect x="15" y="2" width="16" height="8" rx="2" fill="none" stroke="#3e5a85" stroke-width="3"/><rect x="2" y="9" width="42" height="29" rx="4" fill="#3e5a85"/><path d="M23 15v17M14.5 23.5h17" stroke="#fff" stroke-width="5"/></svg></div>
  <h3>Emergency Services</h3>
  <p>It is important to seek medical attention<br>for any eye or eyelid injuries, foreign<br>bodies in the eye, or sudden</p>
  <span class="read">READ MORE</span>
</div>
<div class="abs service" style="left:346px">
  <div class="circle"><svg width="34" height="46" viewBox="0 0 34 46"><circle cx="17" cy="7" r="6" fill="#3e5a85"/><path d="M2 16l8 2h14l8-2M10 18v12h14V18M11 30v14M23 30v14" stroke="#3e5a85" stroke-width="5" fill="none" stroke-linecap="round"/></svg></div>
  <h3>Eye Care for Children</h3>
  <p>Clear vision is essential to a child's early<br>development. The majority of what chil-<br>dren learn early on in a classroom</p>
  <span class="read">READ MORE</span>
</div>
<div class="abs service" style="left:607px">
  <div class="circle"><svg width="62" height="28" viewBox="0 0 62 28"><circle cx="15" cy="15" r="11" fill="none" stroke="#3e5a85" stroke-width="3"/><circle cx="47" cy="15" r="11" fill="none" stroke="#3e5a85" stroke-width="3"/><path d="M26 13q5-5 10 0M4 13 1 8M58 13l3-5" stroke="#3e5a85" stroke-width="3" fill="none"/></svg></div>
  <h3>Eyewear</h3>
  <p>If a comprehensive eye examination<br>indicates that you have a vision problem<br>that can be corrected with prescription</p>
  <span class="read">READ MORE</span>
</div>
<div class="abs service" style="left:878px">
  <div class="circle"><svg width="62" height="40" viewBox="0 0 62 40"><circle cx="17" cy="12" r="10" fill="none" stroke="#3e5a85" stroke-width="3"/><circle cx="45" cy="12" r="10" fill="none" stroke="#3e5a85" stroke-width="3"/><path d="M27 11h8" stroke="#3e5a85" stroke-width="3"/><path d="M31 26c-6-5-16-4-22 4 8-1 15 2 22-2 7 4 14 1 22 2-6-8-16-9-22-4z" fill="#3e5a85"/></svg></div>
  <h3>Eyeglass Repair</h3>
  <p>Eyeglasses are not cheap. If your eye-<br>glasses are broken or damaged, it may<br>be worthwhile to try to have them</p>
  <span class="read">READ MORE</span>
</div>

<div class="abs why-photo" role="img" aria-label="Trial frame glasses resting on an eye chart"></div>
<div class="abs why-head"><span class="mark"></span><h2 class="cond">WHY US?</h2></div>
<ul class="abs why-list">
  <li><svg width="14" height="9" viewBox="0 0 14 9"><path d="M1 4.5Q7-2 13 4.5 7 11 1 4.5z" fill="#555"/><circle cx="7" cy="4.5" r="2" fill="#fff"/></svg><span>We treat you like a VIP - every experience you have with us will leave you knowing you received the VIP treatment</span></li>
  <li><svg width="14" height="9" viewBox="0 0 14 9"><path d="M1 4.5Q7-2 13 4.5 7 11 1 4.5z" fill="#555"/><circle cx="7" cy="4.5" r="2" fill="#fff"/></svg><span>We are here to serve YOU - we offer same day appointments and convenient clinic hours</span></li>
  <li><svg width="14" height="9" viewBox="0 0 14 9"><path d="M1 4.5Q7-2 13 4.5 7 11 1 4.5z" fill="#555"/><circle cx="7" cy="4.5" r="2" fill="#fff"/></svg><span>Our caring doctors are experts in eye care including advanced contact lens fits and the treatment of eye diseases</span></li>
  <li><svg width="14" height="9" viewBox="0 0 14 9"><path d="M1 4.5Q7-2 13 4.5 7 11 1 4.5z" fill="#555"/><circle cx="7" cy="4.5" r="2" fill="#fff"/></svg><span>We have the best trained and friendliest staff devoted to your care</span></li>
  <li><svg width="14" height="9" viewBox="0 0 14 9"><path d="M1 4.5Q7-2 13 4.5 7 11 1 4.5z" fill="#555"/><circle cx="7" cy="4.5" r="2" fill="#fff"/></svg><span>We offer the latest in eye care technology including the Lumora Scan OCT, the Vistrel retinal exam, and Clarion high-definition eyeglass lenses</span></li>
  <li><svg width="14" height="9" viewBox="0 0 14 9"><path d="M1 4.5Q7-2 13 4.5 7 11 1 4.5z" fill="#555"/><circle cx="7" cy="4.5" r="2" fill="#fff"/></svg><span>We are providers for most insurance plans</span></li>
  <li><svg width="14" height="9" viewBox="0 0 14 9"><path d="M1 4.5Q7-2 13 4.5 7 11 1 4.5z" fill="#555"/><circle cx="7" cy="4.5" r="2" fill="#fff"/></svg><span>We have strong relationships and network with the very best retinal, corneal, cataract, and LASIK surgeons in the state</span></li>
</ul>

<section class="abs experts" role="img" aria-label="Soft dark blue close-up of an eye"></section>
<div class="abs section-head on-dark" style="top:2212px"><span class="mark"></span><h2 class="cond">TRUE EXPERTS OF EYE CARE</h2></div>
<p class="abs experts-text">Many people resort to the simple solution of purchasing glasses at a drug store or pharmacy, but it could cost them their vision. Our optometrists are skilled at not only detecting typical refractive errors (nearsightedness, farsightedness, and astigmatism) and prescribing the proper corrective eyewear, but also finding eye diseases in their early stages. You can't get that from a convenience store. Without regularly scheduled eye examinations, you may not realize that you are suffering from an eye disease until it affects your vision and may be more difficult to treat.</p>

<footer class="abs footer"></footer>
<div class="abs partner-badge" role="img" aria-label="Partner association badge"></div>
<div class="abs footer-col quick">
  <h4>QUICK LINKS</h4>
  <ul><li>Vision Services</li><li>Vision Health</li><li>Patient Info</li><li>Patient</li><li>Reviews</li><li>Schedule Appointment</li><li>Contact</li></ul>
</div>
<div class="abs footer-col newsletter">
  <h4>SIGN UP FOR NEWSLETTER</h4>
  <p>Join us today and start celebrate the life of your lost loved one.</p>
  <div class="field" style="margin-top:14px">Enter Name</div>
  <div class="field" style="margin-top:10px;position:relative">Enter Email<span class="subscribe">SUBSCRIBE</span></div>
</div>
<div class="abs footer-col contact">
  <h4>CONTACT US</h4>
  <div class="addr">Bluepine Optics<br>1180 West Harmon Avenue<br>Oklahoma City, OK 73120</div>
  <div class="row"><svg width="16" height="16" viewBox="0 0 16 16"><path d="M3 1l3 3-2 2q2 4 6 6l2-2 3 3-2 2Q6 14 1 3z" fill="none" stroke="#5b7fbf" stroke-width="1.3"/></svg>Phone: 405-555-0174</div>
  <div class="row"><svg width="16" height="12" viewBox="0 0 16 12"><rect x="0.7" y="0.7" width="14.6" height="10.6" fill="none" stroke="#5b7fbf" stroke-width="1.3"/><path d="M1 1l7 6 7-6" fill="none" stroke="#5b7fbf" stroke-width="1.3"/></svg>info@bluepineoptics.example</div>
  <div class="socials"><span></span><span></span><span></span><span></span><span></span></div>
</div>
<div class="abs bottom-bar">©2015 - 2016 Bluepine Optics .. All Rights Reserved.</div>

</body>
</html>
```